VELMORHAVEN

We just changed our name from Quillhacks to Velmorrhaven so we need a new website. have been in the catering &special events business for 36 years . We are an in house caterer with homemade food and best around our name has always hurt us so we changed it and want a new web site to go with it. The current website Quillhacks banquet center .com can be viewed but, is horrible. I have been to many website companies in the past years and have never had a profesinal website. What brides want to see on the web are pictures and I feel they do not necessarily have to be from this facility they can be stock photos that resemble this place.

weddings partys

Business

5+ page

Must have
• pictures
Nice to have
• we have done functions for the king of Jordan on his plane and other famous people including celebrities and stars. This was when we were doing airline catering years ago, but, does not matter if plane or our facility they do not need to know that. Their were many people who have come to us from all over the world for private functions. Consider the possibilities memorable Weddings, exciting anniversaries and birthday parties .

```html
<!DOCTYPE html>
<html lang="en">
<head>
<meta charset="utf-8">
<title>Velmorrhaven Catering</title>
<link href="https://fonts.googleapis.com/css2?family=Arimo:wght@400;700&display=swap" rel="stylesheet">
<style>
:root{
  --red:#f4330d;
  --ink:#1c1c1c;
  --text:#555;
  --muted:#9a9a9a;
  --hero-bg:#efeeea;
  --soft-bg:#f5f5f5;
  --white:#fff;
}
*{margin:0;padding:0;box-sizing:border-box}
html,body{width:1200px;height:3191px;overflow:hidden}
body{position:relative;background:var(--white);font-family:"Arimo",Arial,sans-serif;color:var(--text)}
.abs{position:absolute}
.center{text-align:center;left:0;width:1200px}

/* header */
.brand{left:98px;top:30px;font-size:40px;font-weight:400;color:var(--ink);letter-spacing:-0.5px;white-space:nowrap}
.contact{top:24px;font-size:14px;color:var(--ink);display:flex;align-items:center;gap:10px;white-space:nowrap}
.contact .ico{width:17px;height:17px;background:var(--red);border-radius:3px;display:flex;align-items:center;justify-content:center;flex:none}
.nav-item{top:62px;font-size:13px;color:var(--ink);white-space:nowrap}

/* hero */
.hero{top:100px;left:0;width:1200px;height:479px;background:var(--hero-bg);overflow:hidden}
.hero-title{left:121px;top:176px;font-size:46px;color:var(--ink);font-weight:400;letter-spacing:-0.5px;white-space:nowrap}
.hero-title b{color:var(--red);font-weight:700}
.hero-rule{left:165px;top:252px;width:410px;height:1px;background:#c8c8c8}
.hero-text{left:140px;top:280px;width:470px;text-align:center;font-size:14px;line-height:23px;color:var(--text)}
.occasion{width:128px;height:128px;border-radius:50%;background:var(--red);border:5px solid #fff;box-shadow:0 4px 10px rgba(0,0,0,.18);color:#fff;font-size:14px;display:flex;flex-direction:column;align-items:center;justify-content:center;gap:8px}
.occasion.outline{background:#fff;border:3px solid var(--red);color:var(--red)}
.chef{left:700px;top:115px;width:440px;height:464px;border-radius:46% 54% 0 0/36% 36% 0 0;background:linear-gradient(180deg,#c9beb4,#aa9e94)}
.arrow{top:306px}

/* section headings */
.h2{font-size:29px;font-weight:700;color:var(--ink);letter-spacing:.3px}
.rule{width:60px;height:2px;background:var(--red);left:570px}
.lede{font-size:12.5px;line-height:24px;color:var(--text)}

/* search */
.field{top:819px;height:38px;border:1px solid #ddd;background:#fbfbfb;font-size:12px;color:#aaa;padding:0 12px;display:flex;align-items:center;justify-content:space-between}
.search-btn{top:819px;left:834px;width:166px;height:38px;background:var(--red);color:#fff;font-size:13px;display:flex;align-items:center;justify-content:center}

/* services */
.services{top:932px;left:0;width:1200px;height:441px;background:var(--soft-bg)}
.service-card{top:1149px;width:183px;height:145px;background:#fff;box-shadow:0 2px 8px rgba(0,0,0,.09);display:flex;flex-direction:column;align-items:center;justify-content:center;gap:18px;font-size:14px;color:var(--ink)}

/* events */
.event-photo{top:1536px;width:311px;height:162px}
.event-title{top:1718px;width:311px;text-align:center;font-size:16px;font-weight:700;color:var(--ink)}
.event-text{top:1748px;width:311px;text-align:center;font-size:12px;line-height:24px;color:var(--text)}
.read-more{top:1802px;width:311px;text-align:center;font-size:11.5px;color:var(--red)}

/* testimonial */
.testimonial{top:1894px;left:0;width:1200px;height:387px;background:linear-gradient(180deg,#f83c10,#f02a0a);border-radius:6px 6px 0 0}
.avatar-ring{left:196px;top:2071px;width:136px;height:136px;border-radius:50%;border:2px dashed rgba(255,255,255,.7)}
.avatar{left:206px;top:2081px;width:116px;height:116px;border-radius:50%;border:4px solid #fff;background:linear-gradient(160deg,#e9e3dd,#a79c93)}
.quote{left:443px;top:2080px;width:640px;font-size:13.5px;line-height:26px;color:#fff}
.quote-by{left:776px;top:2176px;font-size:15px;font-weight:700;color:#fff}
.quote-by small{font-size:11px;font-weight:400}
.qmark{font-size:30px;font-weight:700;color:#fff;line-height:1}

/* gallery */
.gallery-tile{top:2288px;width:240px;height:170px}

/* news */
.news-photo{top:2628px;width:204px;height:166px}
.news-meta{top:2644px;font-size:11.5px;color:var(--text);display:flex;gap:26px;align-items:center}
.news-meta span{display:flex;align-items:center;gap:8px}
.news-title{top:2669px;width:245px;font-size:15px;line-height:25px;font-weight:700;color:var(--ink)}
.news-text{top:2726px;width:245px;font-size:12px;line-height:21px;color:var(--text)}

/* footer */
.footer-rule{left:98px;top:2869px;width:1003px;height:2px;background:var(--red)}
.footer-col h4{font-size:16px;font-weight:700;color:var(--ink);letter-spacing:.4px;margin-bottom:14px;white-space:nowrap}
.footer-col li{list-style:none;font-size:12px;color:var(--text);line-height:24.5px;padding-left:28px;position:relative;white-space:nowrap}
.footer-col li::before{content:"»";position:absolute;left:0;color:var(--red);font-size:13px}
.news-input{left:851px;width:250px;height:33px;border:1px solid #ddd;font-size:11px;color:#aaa;padding:0 10px;display:flex;align-items:center}
.submit{left:851px;top:3049px;width:250px;height:32px;background:var(--red);color:#fff;font-size:15px;display:flex;align-items:center;justify-content:center}
.bottom-bar{top:3137px;left:0;width:1200px;height:54px;background:#f2f2f2;font-size:12px;color:var(--muted);display:flex;align-items:center;justify-content:center}
</style>
</head>
<body>

<!-- Header -->
<div class="abs brand">Velmorrhaven</div>
<div class="abs contact" style="left:700px">
  <span class="ico"><svg width="11" height="9" viewBox="0 0 11 9"><rect x=".5" y=".5" width="10" height="8" fill="none" stroke="#fff"/><path d="M.5 .5 5.5 5 10.5 .5" fill="none" stroke="#fff"/></svg></span>
  hello@velmorr.com
</div>
<div class="abs contact" style="left:940px">
  <span class="ico"><svg width="10" height="10" viewBox="0 0 10 10"><path d="M2 1 4 3 3 4.5Q4 6.5 5.5 7L7 6 9 8 7.5 9.5Q2 8 .5 2.5Z" fill="#fff"/></svg></span>
  (888)555 014 2270
</div>
<nav>
  <span class="abs nav-item" style="left:534px">Home</span>
  <span class="abs nav-item" style="left:632px">About us</span>
  <span class="abs nav-item" style="left:747px">Services</span>
  <span class="abs nav-item" style="left:860px">Gallery</span>
  <span class="abs nav-item" style="left:964px">Contact us</span>
  <span class="abs nav-item" style="left:1056px">|</span>
  <svg class="abs" style="left:1086px;top:62px" width="14" height="14" viewBox="0 0 14 14"><circle cx="6" cy="6" r="4.5" fill="none" stroke="#1c1c1c" stroke-width="2"/><path d="M9.5 9.5 13 13" stroke="#1c1c1c" stroke-width="2"/></svg>
</nav>

<!-- Hero -->
<section class="abs hero"></section>
<div class="abs chef" role="img" aria-label="Smiling chef in red hat and scarf with arms crossed"></div>
<div class="abs hero-title">Velmorrhaven <b>Catering</b></div>
<div class="abs hero-rule"></div>
<p class="abs hero-text">We are into catering &amp; special events business for 36 years . We are an inhouse caterer with homemade food.</p>
<div class="abs occasion" style="left:125px;top:362px">
  <svg width="40" height="32" viewBox="0 0 40 32"><circle cx="14" cy="19" r="10" fill="none" stroke="#fff" stroke-width="3"/><circle cx="26" cy="19" r="10" fill="none" stroke="#fff" stroke-width="3"/><path d="M11 4h6l-3 4z" fill="#fff"/></svg>
  WEDDING
</div>
<div class="abs occasion outline" style="left:317px;top:362px">
  <svg width="40" height="32" viewBox="0 0 40 32" fill="none" stroke="#f4330d" stroke-width="2.5"><path d="M8 4 16 8 14 16 8 14Z"/><path d="M32 4 24 8 26 16 32 14Z"/><path d="M11 15 7 28M29 15 33 28"/></svg>
  ANNIVERSARY
</div>
<div class="abs occasion" style="left:481px;top:362px">
  <svg width="36" height="34" viewBox="0 0 36 34" fill="none" stroke="#fff" stroke-width="3"><rect x="4" y="12" width="28" height="20"/><rect x="2" y="8" width="32" height="6"/><path d="M18 8v24M18 8Q10 0 10 6M18 8Q26 0 26 6"/></svg>
  BIRTHDAY
</div>
<svg class="abs arrow" style="left:34px" width="28" height="110" viewBox="0 0 28 110"><path d="M24 2 4 55 24 108" fill="none" stroke="#cfcfcf" stroke-width="2"/></svg>
<svg class="abs arrow" style="left:1138px" width="28" height="110" viewBox="0 0 28 110"><path d="M4 2 24 55 4 108" fill="none" stroke="#cfcfcf" stroke-width="2"/></svg>

<!-- Welcome -->
<h2 class="abs center h2" style="top:650px">WELCOME TO VELMORRHAVEN</h2>
<div class="abs rule" style="top:706px"></div>
<p class="abs lede" style="left:200px;top:738px;width:800px;text-align:center">Contrary to popular belief, Lorem Ipsum is not simply random text. It has roots in a piece of classical Latin literature from 45 BC, making it over 2000 years old. Adrian Hollis, a Latin professor at Larchmont College in Virginia, looked up one of the more obscure</p>
<div class="abs field" style="left:200px;width:217px">Event type
  <svg width="11" height="11" viewBox="0 0 11 11" fill="#999"><rect width="4" height="4"/><rect x="6" width="4" height="4"/><rect y="6" width="4" height="4"/><rect x="6" y="6" width="4" height="4"/></svg></div>
<div class="abs field" style="left:430px;width:217px">Event location
  <svg width="9" height="12" viewBox="0 0 9 12"><path d="M4.5 12 1 6a4 4 0 1 1 7 0Z" fill="#999"/><circle cx="4.5" cy="4.5" r="1.5" fill="#fbfbfb"/></svg></div>
<div class="abs field" style="left:658px;width:166px">Date of the event
  <svg width="11" height="11" viewBox="0 0 11 11"><rect x=".5" y="1.5" width="10" height="9" fill="none" stroke="#999"/><path d="M.5 4h10" stroke="#999"/></svg></div>
<div class="abs search-btn">SEARCH NOW</div>

<!-- Services -->
<section class="abs services"></section>
<h2 class="abs center h2" style="top:1001px">OUR SERVICES</h2>
<div class="abs rule" style="top:1057px"></div>
<p class="abs lede" style="left:300px;top:1072px;width:600px;text-align:center">We offer a variety of services. Come see our Consultant Debbie and she'll make sure your special day is even more special than you have ever imagined.</p>

<div class="abs service-card" style="left:98px">
  <svg width="36" height="38" viewBox="0 0 36 38" fill="#f4330d"><path d="M6 2h2v10h2V2h2v10h2V2h2v12q0 4-4 5v17H9V19q-4-1-4-5V2Z"/><path d="M24 2q8 4 8 16h-4v18h-4Z"/></svg>
  Special Event Catring</div>
<div class="abs service-card" style="left:303px">
  <svg width="36" height="36" viewBox="0 0 36 36" fill="none" stroke="#f4330d" stroke-width="3"><rect x="3" y="15" width="7" height="18"/><path d="M10 17 17 4q4 0 3 6l-1 5h11q3 1 2 4l-3 12q-1 2-3 2H10"/></svg>
  Qualitative Services</div>
<div class="abs service-card" style="left:508px">
  <svg width="40" height="34" viewBox="0 0 40 34" fill="#f4330d"><path d="M4 8h26v10q0 10-13 10T4 18Z"/><path d="M30 11h3q5 0 5 5t-6 5h-3" fill="none" stroke="#f4330d" stroke-width="3"/><rect x="2" y="30" width="32" height="3"/></svg>
  Good Taste</div>
<div class="abs service-card" style="left:713px">
  <svg width="36" height="36" viewBox="0 0 36 36"><circle cx="18" cy="18" r="15" fill="none" stroke="#f4330d" stroke-width="4"/><path d="M18 9v10h7" fill="none" stroke="#f4330d" stroke-width="3.5"/></svg>
  24/7 Service</div>
<div class="abs service-card" style="left:918px">
  <svg width="36" height="36" viewBox="0 0 36 36" fill="none" stroke="#f4330d" stroke-width="3"><rect x="3" y="6" width="30" height="27"/><path d="M3 13h30M11 2v8M25 2v8M9 19h4M16 19h4M23 19h4M9 26h4M16 26h4M23 26h4"/></svg>
  All Occasions</div>

<!-- Events -->
<h2 class="abs center h2" style="top:1442px">EVENTS OVERVIEW</h2>
<div class="abs rule" style="top:1497px"></div>
<div class="abs event-photo" style="left:98px;background:linear-gradient(180deg,#2a2016,#6b4a22 55%,#1b1510)" role="img" aria-label="Dimly lit banquet lounge with warm lights"></div>
<div class="abs event-photo" style="left:445px;background:linear-gradient(180deg,#3a3020,#c9b79a 45%,#8b3a22 75%,#2a1c12)" role="img" aria-label="Buffet table with fresh food and fruit"></div>
<div class="abs event-photo" style="left:790px;background:linear-gradient(180deg,#a48e66,#e7dcc6 45%,#8a7350)" role="img" aria-label="Bright ballroom with chandeliers and set tables"></div>

<div class="abs event-title" style="left:98px">SED PERSPICIATIS UNDE OMNIS</div>
<div class="abs event-title" style="left:445px">SED PERSPICIATIS UNDE OMNIS</div>
<div class="abs event-title" style="left:790px">SED PERSPICIATIS UNDE OMNIS</div>
<p class="abs event-text" style="left:98px">Lorem ipsum dolor sit amet, consectetuer. Proin gravida nibh vel velit auctor aliquet. the far Aenean</p>
<p class="abs event-text" style="left:445px">Lorem ipsum dolor sit amet, consectetuer. Proin gravida nibh vel velit auctor aliquet. the far Aenean</p>
<p class="abs event-text" style="left:790px">Lorem ipsum dolor sit amet, consectetuer. Proin gravida nibh vel velit auctor aliquet. the far Aenean</p>
<div class="abs read-more" style="left:98px">Read More</div>
<div class="abs read-more" style="left:445px">Read More</div>
<div class="abs read-more" style="left:790px">Read More</div>

<!-- Testimonial -->
<section class="abs testimonial"></section>
<h2 class="abs center h2" style="top:1964px;color:#fff">OUR CLIENT TESTIMONIAL</h2>
<div class="abs rule" style="top:2020px;background:#fff"></div>
<div class="abs avatar-ring"></div>
<div class="abs avatar" role="img" aria-label="Portrait of a bride in a white gown"></div>
<div class="abs qmark" style="left:408px;top:2082px">&ldquo;</div>
<p class="abs quote">Contrary to popular belief, Lorem Ipsum is not simply random text. It has roots in a piece of classical Latin literature from 45 BC, making it over 2000 years old. Adrian Hollis, a Latin professor at Larchmont College Contrary to popular belief, Lorem Ipsum is not simply random text.</p>
<div class="abs qmark" style="left:988px;top:2138px">&rdquo;</div>
<div class="abs quote-by">- Elena Marsh <small>( CEO )</small></div>

<!-- Gallery -->
<div class="abs gallery-tile" style="left:0;background:linear-gradient(180deg,#5b5550,#b8ada2 60%,#6c6259)" role="img" aria-label="Reception hall with round dining tables"></div>
<div class="abs gallery-tile" style="left:240px;background:linear-gradient(180deg,#2e2822,#9c8a74 55%,#4a3a2c)" role="img" aria-label="Chafing dishes on a buffet line"></div>
<div class="abs gallery-tile" style="left:480px;background:linear-gradient(180deg,#1f2630,#7d8896 55%,#d9dee6)" role="img" aria-label="Snowy evening garden outside the venue"></div>
<div class="abs gallery-tile" style="left:720px;background:linear-gradient(180deg,#2a1560,#8a3fd0 50%,#1b0f3a)" role="img" aria-label="Dance floor with purple party lights"></div>
<div class="abs gallery-tile" style="left:960px;background:linear-gradient(180deg,#3c4a2e,#c8b48c 50%,#a8341e 80%,#2e2418)" role="img" aria-label="Decorated buffet with ice sculpture"></div>

<!-- Latest news -->
<h2 class="abs center h2" style="top:2525px">OUR LATEST NEWS</h2>
<div class="abs rule" style="top:2580px"></div>

<div class="abs news-photo" style="left:98px;background:linear-gradient(180deg,#1a1f6a,#4d5ed8 55%,#151840)" role="img" aria-label="Guests at an evening party under blue lights"></div>
<div class="abs news-meta" style="left:321px">
  <span><svg width="9" height="10" viewBox="0 0 9 10" fill="#f4330d"><circle cx="4.5" cy="2.5" r="2.5"/><path d="M0 10q0-5 4.5-5T9 10Z"/></svg>John Doe</span>
  <span><svg width="10" height="10" viewBox="0 0 10 10"><rect x=".5" y="1.5" width="9" height="8" fill="none" stroke="#f4330d"/><path d="M.5 4h9" stroke="#f4330d"/></svg>30/04/2016</span>
</div>
<div class="abs news-title" style="left:321px">Sed ut perspiciatis unde the is iste natus error</div>
<p class="abs news-text" style="left:321px">Lorem ipsum dolor sit amet, consectetur adi-piscing elit, sed do eiusmod tempor incididunt ut labore et dolore magna aliqua.</p>

<div class="abs news-photo" style="left:626px;background:linear-gradient(180deg,#2c261f,#8d7b64 55%,#3a3028)" role="img" aria-label="Elegant banquet room set for dinner"></div>
<div class="abs news-meta" style="left:847px">
  <span><svg width="9" height="10" viewBox="0 0 9 10" fill="#f4330d"><circle cx="4.5" cy="2.5" r="2.5"/><path d="M0 10q0-5 4.5-5T9 10Z"/></svg>John Doe</span>
  <span><svg width="10" height="10" viewBox="0 0 10 10"><rect x=".5" y="1.5" width="9" height="8" fill="none" stroke="#f4330d"/><path d="M.5 4h9" stroke="#f4330d"/></svg>30/04/2016</span>
</div>
<div class="abs news-title" style="left:847px">Sed ut perspiciatis unde the mnis iste natus error</div>
<p class="abs news-text" style="left:847px">Lorem ipsum dolor sit amet, consectetur adi-piscing elit, sed do eiusmod tempor incididunt ut labore et dolore magna aliqua.</p>

<!-- Footer -->
<div class="abs footer-rule"></div>
<div class="abs footer-col" style="left:98px;top:2926px">
  <h4>COMPANY</h4>
  <ul><li>Home</li><li>About</li><li>Services</li><li>Gallery</li><li>Contact us</li></ul>
</div>
<div class="abs footer-col" style="left:262px;top:2926px">
  <h4>SERVICES</h4>
  <ul><li>Weddings</li><li>Banquets</li><li>Fund Raisers</li><li>Retirement Parties</li></ul>
</div>
<div class="abs footer-col" style="left:462px;top:2924px">
  <h4>OUR POLICY</h4>
  <ul><li>Help &amp; Contact</li><li>Register entry</li><li>Affiliates</li></ul>
</div>
<div class="abs footer-col" style="left:653px;top:2926px">
  <h4>SUPPORT</h4>
  <ul><li>Get In Touch</li><li>Support Forums</li><li>Knowledge Base</li><li>Request a Quote</li></ul>
</div>
<div class="abs footer-col" style="left:851px;top:2926px"><h4>NEWSLETTER SIGNUP</h4></div>
<div class="abs news-input" style="top:2966px">Name</div>
<div class="abs news-input" style="top:3007px">Email</div>
<div class="abs submit">SUBMIT NOW</div>

<div class="abs bottom-bar">Copyrights@2017Company Name, all rights reserved</div>

</body>
</html>
```